Tessel PR (young, fun PR agency) needs a Business Card Design

We need a new business card design that reflects who we are as a company. We're a Sydney-based PR agency that's six years old with clients including Blue Heron, Duneprint, OLVEN, Lou Carvell etc. - just check out our website for more info: www.tesselpr.com.au. We would like to see designs that bring to life our company name and what we do (generating media coverage for brands on TV, radio, online and in newspapers and magazines). We don't want a corporate style card but one that people take notice of and think 'wow that's a cool business card'. It doesn't have to be the standard rectangle shape and can incorporate humour.

Target Market(s)

Clients (generally cool/creative types) and media

Industry/Entity Type

Business

Requirements
Must have
• The card must feature our business logo (which can be updated if you like) and use both sides.
Nice to have
• The card could feature a cool illustration

```html
<!DOCTYPE html>
<html lang="en">
<head>
<meta charset="utf-8">
<title>Tessel PR — Business Card</title>
<link rel="stylesheet" href="https://fonts.googleapis.com/css2?family=Archivo+Narrow:wght@700&family=Jost:wght@700&display=swap">
<style>
  :root {
    --backdrop: #3b3b3b;
    --card-white: #ffffff;
    --brand-orange: #f5ae4e;
    --ink: #1a1a1a;
  }
  html, body {
    margin: 0;
    padding: 0;
    width: 1200px;
    height: 569px;
    overflow: hidden;
    background: var(--backdrop);
  }
  .canvas {
    position: relative;
    width: 1200px;
    height: 569px;
  }
  .card {
    position: absolute;
    top: 150px;
    width: 489px;
    height: 270px;
    overflow: hidden;
  }
  .card--front { left: 86px; background: var(--card-white); }
  .card--back { left: 625px; background: var(--brand-orange); }

  .holder-name {
    position: absolute;
    left: 24px;
    top: 15px;
    margin: 0;
    font: 700 10px/1 "Jost", sans-serif;
    letter-spacing: 0.3px;
    color: var(--ink);
  }
  .brand-name {
    position: absolute;
    left: 28px;
    top: 102px;
    margin: 0;
    font: 700 37px/1 "Archivo Narrow", sans-serif;
    letter-spacing: 0.5px;
    color: var(--ink);
  }
  .brand-mark {
    position: absolute;
    left: 229px;
    top: 102px;
  }
  .tagline-band {
    position: absolute;
    left: 22px;
    top: 144px;
    width: 252px;
    height: 19px;
    background: var(--brand-orange);
  }
  .tagline {
    position: absolute;
    left: 6px;
    top: 3px;
    margin: 0;
    font: 700 12px/1 "Archivo Narrow", sans-serif;
    letter-spacing: 0.4px;
    color: var(--ink);
  }
  .edge-shape {
    position: absolute;
    top: 0;
  }
  .card--front .edge-shape { right: 0; }
  .card--back .edge-shape { left: 0; }

  .contact {
    position: absolute;
    right: 22px;
    top: 95px;
    margin: 0;
    font: 700 10.5px/15.2px "Jost", sans-serif;
    text-align: right;
    font-style: normal;
    color: var(--ink);
  }
</style>
</head>
<body>
<main class="canvas">
  <section class="card card--front" aria-label="Card front">
    <p class="holder-name">MARCUS</p>
    <h1 class="brand-name">TESSEL PR</h1>
    <svg class="brand-mark" width="68" height="68" viewBox="0 0 68 68" aria-hidden="true">
      <circle cx="34" cy="34" r="31" fill="none" stroke="var(--ink)" stroke-width="3"/>
    </svg>
    <div class="tagline-band">
      <p class="tagline">PUBLIC RELATIONS</p>
    </div>
    <svg class="edge-shape" width="135" height="270" viewBox="0 0 135 270" aria-hidden="true">
      <path d="M135 0 A135 135 0 0 0 135 270 Z" fill="var(--brand-orange)"/>
    </svg>
  </section>

  <section class="card card--back" aria-label="Card back">
    <svg class="edge-shape" width="135" height="270" viewBox="0 0 135 270" aria-hidden="true">
      <path d="M0 0 A135 135 0 0 1 0 270 Z" fill="var(--card-white)"/>
    </svg>
    <address class="contact">
      118 Bay Avenue<br>
      Albany, NY 12209<br>
      212-555-0148<br>
      marcus@tesselpr.com.au<br>
      www.tesselpr.com.au
    </address>
  </section>
</main>
</body>
</html>
```